PageForge Design Project for lornabethwickes.com.au

Update
PLEASE NOTE ...Coding Required

I need a simple website to display my art. There will be 4 different categories - FloraGrandis (botanical art), Oceanlife, Travel Sketchbook, Portraits. There needs to be room for an introduction to me and my work,photos of my studio and views from here and a description of each individual piece. I will probably display no more than 10 pieces in category. Obviously I need to change photos on a regular basis.

I would also like to include a CoinPort button to be connected to my CoinPort account.

I have already started to do a website on PageForge but am finding it too hard to do.

Thank you

Lorna
Updates

Reason: I have provided a deadline extension as I feel the initial lead up time could be too short. Hope that helps you. Lorna

Dear designers. Thankyou all so much for submitting some beautiful designs. I will spend time this weekend evaluating them but as the closing date is January 19, I will not make final decisions until then.  You have probably received an update by now butI  just want to mention that Coding is required.

Cheers

Lorna

Thank you Designers for your patience.  I have been advised by ArtistHive that I cannot make a decision until the deadline has passed, so will let you know on Saturday.

Thank you.
Lorna.

Target Market(s)

35 to 75 who want to buy art and very personal gifts

Industry/Entity Type

Travel

Requirements
Must have
• Ability to change photos often. Modern, elegant, streamlined
Nice to have
• The colour green, an elegant font - sans serif and definitely not courier; room for a photo of me (maybe), and an interesting headline font
Should not have
• quirky, cartooney, retro.

```html
<!DOCTYPE html>
<html lang="en">
<head>
<meta charset="utf-8">
<title>Lorna Bethwickes – Art</title>
<link rel="stylesheet" href="https://fonts.googleapis.com/css2?family=Yanone+Kaffeesatz:wght@400;600&family=Dancing+Script:wght@600&family=Arimo:wght@400;700&display=swap">
<style>
:root{
  --sky:#d9f0fb;
  --sky-deep:#bfe6f8;
  --cyan:#1aa6e0;
  --magenta:#d416b0;
  --magenta-dark:#b00e92;
  --paper:#f3f5f7;
  --card:#f0f0f0;
  --ink:#222;
  --body:#333;
  --navy:#0f5aa0;
  --footer:#151515;
  --pink:#e8157d;
}
*{box-sizing:border-box;margin:0;padding:0}
html,body{width:931px;height:1200px;overflow:hidden}
body{position:relative;font-family:Arimo,Arial,sans-serif;color:var(--body);
  background:linear-gradient(180deg,var(--sky-deep) 0,var(--sky) 60px,#eef7fc 140px,var(--paper) 330px,#f7f7f8 800px,#ececee 1090px)}
.abs{position:absolute}

/* header */
.brand{left:91px;top:42px;font-family:Arimo,Arial,sans-serif;font-weight:700;font-size:33px;line-height:40px;color:var(--cyan);letter-spacing:-0.5px;white-space:nowrap}
.social{display:flex;gap:7px;align-items:center}
.social-item{display:flex;align-items:center;gap:3px;font-size:9.5px;color:#444;font-family:Arimo,Arial,sans-serif;white-space:nowrap}
.social-dot{width:13px;height:13px;border-radius:50%;background:var(--cyan);flex:none}
.social-top{left:572px;top:18px}
.consult{left:579px;top:70px;font-family:'Yanone Kaffeesatz',sans-serif;font-size:17px;line-height:20px;color:#444;letter-spacing:.5px;font-weight:600;white-space:nowrap}
.consult-phone{left:685px;top:68px;font-size:18px;line-height:22px;font-weight:700;color:var(--cyan);white-space:nowrap}

/* nav */
.main-nav{left:83px;top:114px;width:734px;height:32px;background:linear-gradient(180deg,#e02cc0,var(--magenta) 60%,var(--magenta-dark));
  box-shadow:0 8px 6px -4px rgba(0,0,0,.35);display:flex;align-items:center;justify-content:center}
.main-nav a{font-family:'Yanone Kaffeesatz',sans-serif;font-size:13.5px;color:#fff;text-decoration:none;letter-spacing:.4px;padding:0 24px}
.main-nav .sep{color:#fff;font-size:12px}

/* slider */
.slider{left:85px;top:166px;width:729px;height:325px;background:#fff;box-shadow:0 10px 8px -6px rgba(0,0,0,.35)}
.slide-left{position:absolute;left:4px;top:4px;width:400px;height:317px;background:radial-gradient(ellipse at 30% 45%,#fffdf4,#fbf3dc 60%,#f4eee2)}
.slide-art{position:absolute;left:404px;top:4px;width:321px;height:317px;background:radial-gradient(circle at 50% 45%,#f3c8d8 0,#8aa55a 35%,#5c7f38 60%,#f4f3ee 85%)}
.slide-title{position:absolute;left:62px;top:104px;font-family:'Dancing Script',cursive;font-size:38px;line-height:36px;color:var(--cyan);text-shadow:0 2px 3px rgba(0,0,0,.25)}
.arrow{width:32px;height:37px}
.arrow-left{left:83px;top:313px}
.arrow-right{left:784px;top:313px}
.dots{left:416px;top:505px;display:flex;gap:6px}
.dot{width:9px;height:9px;border-radius:50%;background:var(--pink)}
.dot.active{background:#222}

/* welcome */
.welcome{left:90px;top:540px;width:488px}
.welcome h1{font-weight:400;color:var(--cyan);font-size:13px;margin-bottom:8px}
.welcome h1 span{font-size:18px}
.welcome p{font-size:9.1px;line-height:14.5px;color:var(--ink);margin-bottom:14.5px}
.read-more{font-size:8.5px;font-weight:700;color:var(--magenta);display:inline-flex;align-items:center;gap:3px}
.read-more::after{content:"";border-left:4px solid var(--magenta);border-top:4px solid transparent;border-bottom:4px solid transparent}
.profile{left:597px;top:544px;width:216px;height:249px;background:#fff;border:1px solid #ddd;box-shadow:0 1px 4px rgba(0,0,0,.2)}
.profile-photo{position:absolute;left:5px;top:5px;width:206px;height:183px;background:linear-gradient(180deg,#3d3a36,#b88a5f 55%,#e6c9a8)}
.profile-name{position:absolute;left:5px;top:188px;width:206px;height:56px;background:#f2f2f2;font-family:'Yanone Kaffeesatz',sans-serif;font-weight:600;font-size:29px;color:var(--navy);text-align:center;line-height:56px;white-space:nowrap}

/* works */
.works-head{left:83px;top:822px;width:734px;display:flex;align-items:center;gap:14px}
.works-head .rule{flex:1;height:2px;background:#d6d6d6;border-bottom:1px solid #fff}
.works-head h2{font-weight:400;font-size:11.5px;letter-spacing:.5px;color:#444}
.work-card{top:856px;width:170px;height:224px;background:var(--card);border:1px solid #e2e2e2;box-shadow:0 6px 6px -4px rgba(0,0,0,.25)}
.work-card h3{height:36px;line-height:36px;text-align:center;font-size:12px;font-weight:700;color:var(--ink);border-bottom:1px solid #dedede}
.work-thumb{position:absolute;left:10px;top:46px;width:151px;height:150px}
.work-card .read-more{position:absolute;left:10px;top:204px}

/* footer */
.site-footer{left:0;top:1096px;width:931px;height:104px;background:var(--footer);color:#fff}
.footer-title{font-size:12px;top:22px;white-space:nowrap}
.newsletter{left:88px;top:40px;width:197px;height:23px;background:#fdf2f8;font-size:8.5px;color:#333;padding:6px 9px;display:flex;justify-content:space-between;align-items:center}
.footer-social{left:428px;top:40px;width:190px;display:grid;grid-template-columns:80px 100px;row-gap:5px;column-gap:8px}
.footer-social .social-item{color:#ddd}
.contact{left:635px;top:42px;font-size:10.5px;line-height:16px;white-space:nowrap}
.copyright{left:0;top:86px;width:931px;text-align:center;font-size:7.5px;color:#ddd}
</style>
</head>
<body>

<header>
  <div class="abs brand">Lorna Bethwickes</div>
  <div class="abs social social-top">
    <span class="social-item"><span class="social-dot"></span>Linkbook</span>
    <span class="social-item"><span class="social-dot"></span>Chirper</span>
    <span class="social-item"><span class="social-dot"></span>Circlesphere</span>
    <span class="social-item"><span class="social-dot"></span>FeedLine</span>
  </div>
  <div class="abs consult">FREE CONSULTAION</div>
  <div class="abs consult-phone">877-555-0142</div>
</header>

<nav class="abs main-nav">
  <a href="#">HOME</a><span class="sep">|</span>
  <a href="#">ABOUT ME</a><span class="sep">|</span>
  <a href="#">FLORAGRANDIS</a><span class="sep">|</span>
  <a href="#">OCEANLIFE</a><span class="sep">|</span>
  <a href="#">TRAVEL SKETCHBOOK</a><span class="sep">|</span>
  <a href="#">PORTRAITS</a><span class="sep">|</span>
  <a href="#">CONTACT</a>
</nav>

<section class="abs slider">
  <div class="slide-left">
    <div class="slide-title">Explore My<br>Dream Creations</div>
  </div>
  <div class="slide-art" role="img" aria-label="Botanical painting of a frangipani sprig with pink flowers and green leaves"></div>
</section>
<svg class="abs arrow arrow-left" viewBox="0 0 32 37" aria-hidden="true">
  <rect x="0" y="0" width="32" height="33" rx="3" fill="#1e8fd6"/>
  <rect x="0" y="30" width="32" height="7" rx="2" fill="#0d5f99"/>
  <path d="M21 9 L10 16.5 L21 24 Z" fill="#0a3e66"/>
</svg>
<svg class="abs arrow arrow-right" viewBox="0 0 32 37" aria-hidden="true">
  <rect x="0" y="0" width="32" height="33" rx="3" fill="#1e8fd6"/>
  <rect x="0" y="30" width="32" height="7" rx="2" fill="#0d5f99"/>
  <path d="M11 9 L22 16.5 L11 24 Z" fill="#0a3e66"/>
</svg>
<div class="abs dots"><span class="dot active"></span><span class="dot"></span><span class="dot"></span><span class="dot"></span><span class="dot"></span></div>

<section class="abs welcome">
  <h1>Welcome to <span>Lorna Bethwickes’s Dream World</span></h1>
  <p>Lorem ipsum dolor sit amet, consectetur adipiscing elit. Fusce in dui tortor. Etiam vitae adipiscing sapien. Mauris ornare, nisl ultricies semper molestie, sem elit auctor arcu, et accumsan nibh nunc eu est. Suspendisse tempus magna ut augue eleifend laoreet. Donec accumsan cursus faucibus. Aliquam faucibus tellus a mi sollicitudin vel iaculis diam sagittis. Suspendisse ac luctus nunc. Vivamus velit nulla, luctus ac adipiscing et, ultrices vel tortor.</p>
  <p>Pellentesque habitant morbi tristique senectus et netus et malesuada fames ac turpis egestas. Cras vel adipiscing justo. Sed semper vulputate lacus sed interdum. Nullam quis lacus vitae purus lobortis bibendum non at libero. Pellentesque sed lorem nulla.Lorem ipsum dolor sit amet, consectetur adipiscing elit. Fusce in dui tortor. Etiam vitae adipiscing sapien. Mauris ornare, nisl ultricies semper molestie, sem elit auctor arcu, et accumsan nibh nunc eu est. Suspendisse tempus magna ut augue eleifend laoreet. Donec accumsan cursus faucibus. Aliquam faucibus tellus a mi sollicitudin vel iaculis diam sagittis. Suspend-isse ac luctus nunc. Vivamus velit nulla, luctus ac adipiscing et, ultrices vel tortor.</p>
  <p>Pellentesque habitant morbi tristique senectus et netus et malesuada fames ac turpis egestas. Cras vel adipiscing justo. Sed semper vulputate lacus sed interdum. Nullam quis lacus vitae purus lobortis bibendum non at libero.</p>
  <span class="read-more">Read More</span>
</section>

<aside class="abs profile">
  <div class="profile-photo" role="img" aria-label="Portrait photo of the artist"></div>
  <div class="profile-name">LORNA BETHWICKES</div>
</aside>

<div class="abs works-head"><span class="rule"></span><h2>MY RECENT WORKS</h2><span class="rule"></span></div>

<article class="abs work-card" style="left:83px">
  <h3>FLORAGRANDIS</h3>
  <div class="work-thumb" role="img" aria-label="Watercolour of a small insect among daisies" style="background:radial-gradient(circle at 50% 45%,#f7f6ea,#c9d6b4 60%,#a7b98c)"></div>
  <span class="read-more">Read More</span>
</article>
<article class="abs work-card" style="left:268px">
  <h3>OCEANLIFE</h3>
  <div class="work-thumb" role="img" aria-label="Red jellyfish drifting in dark water" style="background:radial-gradient(circle at 45% 45%,#6a1b2c,#2a0a14 55%,#0c0608)"></div>
  <span class="read-more">Read More</span>
</article>
<article class="abs work-card" style="left:453px">
  <h3>TRAVEL SKETCHBOOK</h3>
  <div class="work-thumb" role="img" aria-label="Coloured sketch of a crowd of travellers on a hillside" style="background:linear-gradient(160deg,#e6dcc4,#c9b896 55%,#8d7a5c)"></div>
  <span class="read-more">Read More</span>
</article>
<article class="abs work-card" style="left:637px">
  <h3>PORTRAITS</h3>
  <div class="work-thumb" role="img" aria-label="High-contrast black and white portrait study" style="background:linear-gradient(135deg,#1a1a1a,#6e6e6e 50%,#cfcfcf)"></div>
  <span class="read-more">Read More</span>
</article>

<footer class="abs site-footer">
  <div class="abs footer-title" style="left:88px">Subscribe Newsletter</div>
  <div class="abs newsletter">Type your email id here
    <svg width="16" height="14" viewBox="0 0 16 14" aria-hidden="true"><path d="M1 7 L6 12 L15 1" fill="none" stroke="#5aa318" stroke-width="3" stroke-linecap="round" stroke-linejoin="round"/></svg>
  </div>
  <div class="abs footer-title" style="left:428px">Find Us</div>
  <div class="abs footer-social">
    <span class="social-item"><span class="social-dot"></span>Linkbook</span>
    <span class="social-item"><span class="social-dot"></span>Chirper</span>
    <span class="social-item"><span class="social-dot"></span>Circlesphere</span>
    <span class="social-item"><span class="social-dot"></span>FeedLine</span>
  </div>
  <div class="abs footer-title" style="left:633px">Contact Us</div>
  <div class="abs contact">Toll Free : 877-555-0187<br>Email : info@lornabethwickes.com</div>
  <div class="abs copyright">© 2013, All Rights Reserved, http://www.lornabethwickes.com</div>
</footer>

</body>
</html>
```